This is for a poster that will be hanging in the window of a Men's Suit Store in the mall:
Size 4 feet wide by 6 feet high
Main point is: A sale on "Suits" or "Men's Suits" at 40%-60% off ( the 40%-60% off should be the focal point)
Some words that can be used are "Sale" or "Clearance Sale"
Some key words that can be used to make it urgent are "limited time offer" or something similar.
You can get creative, the point is for the customer to want to come into the store and buy a suit right away.
You may use a graphic (picture of a man in a suit). It is not necessary but if it looks good you can use it. (If you do use a picture, it should be of a modern fit or slim fit suit)
Sorry, the initial brief somehow got deleted from the project. Please see the updated brief.
Thanks
Reason: Project was closed for some reason, extended to give enough time to complete
Target Market(s)
Mostly Men ages 35-55
Industry/Entity Type
Store
Colors
Designer to choose colors to be used in the design.

```html
<!DOCTYPE html>
<html lang="en">
<head>
<meta charset="utf-8">
<title>Hallam Menswear – Suit Sale Poster</title>
<link rel="stylesheet" href="https://fonts.googleapis.com/css2?family=Arimo:wght@400;700&family=Oswald:wght@700&family=Archivo+Black&display=swap">
<style>
  :root {
    --backdrop: #353533;
    --poster-edge: #ffffff;
    --ink: #000000;
    --gold: #e6b312;
    --rust: #d2522a;
    --white: #ffffff;
  }
  html, body {
    margin: 0;
    padding: 0;
    width: 1200px;
    height: 900px;
    overflow: hidden;
    background: var(--backdrop);
  }
  .poster {
    position: absolute;
    left: 317px;
    top: 25px;
    width: 563px;
    height: 846px;
    border: 2px solid var(--poster-edge);
    background: var(--gold);
    overflow: hidden;
  }
  .header-band {
    position: absolute;
    left: 0;
    top: 0;
    width: 100%;
    height: 95px;
    background: var(--ink);
  }
  .brand {
    position: absolute;
    left: 24px;
    top: 20px;
    display: flex;
    align-items: center;
    gap: 10px;
    color: var(--white);
    font-family: "Arimo", Arial, sans-serif;
    font-weight: 400;
  }
  .brand-mark {
    width: 14px;
    height: 14px;
    background: var(--white);
  }
  .brand-name {
    font-size: 26px;
    line-height: 1;
  }
  .suit-figure {
    position: absolute;
    left: 44px;
    top: 100px;
    width: 477px;
    height: 750px;
    display: block;
  }
  .offer {
    position: absolute;
    left: 0;
    width: 100%;
    margin: 0;
    text-align: center;
    line-height: 1;
    white-space: nowrap;
  }
  .offer-product {
    top: 433px;
    font-family: "Arimo", Arial, sans-serif;
    font-weight: 700;
    font-size: 37px;
    color: var(--gold);
  }
  .offer-discount {
    top: 483px;
    font-family: "Oswald", "Arial Narrow", sans-serif;
    font-weight: 700;
    font-size: 64px;
    letter-spacing: -1px;
    color: var(--rust);
    transform: scaleY(1.22);
  }
  .offer-sale {
    top: 566px;
    font-family: "Archivo Black", "Arial Black", sans-serif;
    font-size: 96px;
    color: var(--gold);
  }
  .offer-urgency {
    top: 665px;
    font-family: "Arimo", Arial, sans-serif;
    font-weight: 700;
    font-size: 24px;
    color: var(--rust);
  }
</style>
</head>
<body>
  <main class="poster">
    <header class="header-band">
      <div class="brand">
        <span class="brand-name">hallam menswear</span>
        <span class="brand-mark"></span>
      </div>
    </header>

    <svg class="suit-figure" viewBox="0 0 477 750" role="img" aria-label="Black suit jacket with shirt and tie hanging on a wooden hanger">
      <path d="M0 750 L0 150 Q0 110 40 100 L160 40 Q238 0 317 40 L437 100 Q477 110 477 150 L477 750 Z" fill="var(--ink)"/>
    </svg>

    <p class="offer offer-product">‘Men's Suits’ at</p>
    <p class="offer offer-discount">40%-60% OFF</p>
    <p class="offer offer-sale">SALE</p>
    <p class="offer offer-urgency">LIMITED TIME OFFER</p>
  </main>
</body>
</html>
```